Delivery restaurant business needs a "product insert" card

We need to design product insert cards in bags with food to be delivered to the customer. The cards will be 5 x 7 postcards. We know what words and elements we want on the card, but need help in designing it. We have a sample/draft (attached) of what we want it to look like but are not married to the idea and are open to a completely different direction

Requirements
Must have
• I would like the design to be elegant and playful as in the sampe picture

```html
<!DOCTYPE html>
<html lang="en">
<head>
<meta charset="utf-8">
<title>Just for you! – Insert Card</title>
<link href="https://fonts.googleapis.com/css2?family=Rubik:wght@700&family=Sniglet&display=swap" rel="stylesheet">
<style>
  :root {
    --card-brown: #a47f60;
    --ink-white: #ffffff;
    --ornament-glow: #d9c4b0;
    --icon-tone: #b08d70;
  }
  html, body {
    margin: 0;
    padding: 0;
    width: 1200px;
    height: 848px;
    overflow: hidden;
    background: var(--card-brown);
  }
  .card {
    position: relative;
    width: 1200px;
    height: 848px;
    background: var(--card-brown);
    color: var(--ink-white);
  }
  .card-frame {
    position: absolute;
    left: 20px;
    top: 20px;
    width: 1156px;
    height: 805px;
    border: 2px solid var(--ink-white);
  }
  .header-art {
    position: absolute;
    left: 0;
    top: 0;
  }
  .card-title {
    position: absolute;
    left: 0;
    width: 1200px;
    top: 118px;
    margin: 0;
    text-align: center;
    font-family: "Sniglet", "Nunito", sans-serif;
    font-weight: 400;
    font-size: 37px;
    line-height: 48px;
    letter-spacing: 1px;
  }
  .ingredient {
    position: absolute;
    height: 70px;
  }
  .ingredient-icon {
    position: absolute;
    left: 0;
    top: 0;
  }
  .ingredient-name {
    position: absolute;
    left: 80px;
    top: 50%;
    transform: translateY(-50%);
    margin: 0;
    font-family: "Rubik", "Arial", sans-serif;
    font-weight: 700;
    font-size: 23px;
    line-height: 31px;
    letter-spacing: 0.3px;
    white-space: nowrap;
  }
  .ingredient-line {
    position: absolute;
    top: 42px;
    height: 3px;
    width: 172px;
    background: var(--ink-white);
  }
  .col-left .ingredient-line { left: 233px; }
  .col-right .ingredient-line { left: 272px; }
</style>
</head>
<body>
<main class="card">
  <div class="card-frame"></div>

  <svg class="header-art" width="1200" height="240" viewBox="0 0 1200 240">
    <defs>
      <radialGradient id="flourish-glow" cx="50%" cy="50%" r="50%">
        <stop offset="0%" stop-color="var(--ornament-glow)" stop-opacity="0.55"/>
        <stop offset="100%" stop-color="var(--ornament-glow)" stop-opacity="0"/>
      </radialGradient>
    </defs>
    <ellipse role="img" aria-label="Decorative scroll flourish above the title" cx="595" cy="82" rx="128" ry="24" fill="url(#flourish-glow)"/>
    <ellipse role="img" aria-label="Decorative scroll flourish below the title" cx="595" cy="201" rx="232" ry="22" fill="url(#flourish-glow)"/>
    <ellipse role="img" aria-label="Small decorative flourish at left of title" cx="336" cy="143" rx="38" ry="19" fill="url(#flourish-glow)"/>
    <ellipse role="img" aria-label="Small decorative flourish at right of title" cx="864" cy="143" rx="38" ry="19" fill="url(#flourish-glow)"/>
    <g stroke="var(--ink-white)" stroke-linecap="round">
      <line x1="380" y1="108.5" x2="485" y2="108.5" stroke-width="3"/>
      <line x1="704" y1="108.5" x2="815" y2="108.5" stroke-width="3"/>
      <line x1="378" y1="142.5" x2="439" y2="142.5" stroke-width="2"/>
      <line x1="761" y1="142.5" x2="822" y2="142.5" stroke-width="2"/>
      <line x1="380" y1="168" x2="815" y2="168" stroke-width="1.5"/>
      <line x1="380" y1="175.5" x2="815" y2="175.5" stroke-width="3"/>
    </g>
  </svg>

  <h1 class="card-title">Just for you!</h1>

  <section class="col-left">
    <div class="ingredient" style="left:120px; top:291px;">
      <svg class="ingredient-icon" width="70" height="70" viewBox="0 0 70 70"><circle cx="35" cy="35" r="32" fill="none" stroke="var(--ink-white)" stroke-width="2"/><circle role="img" aria-label="Line drawing of a chicken" cx="35" cy="35" r="24" fill="var(--icon-tone)"/></svg>
      <p class="ingredient-name">CHICKEN</p>
      <span class="ingredient-line"></span>
    </div>
    <div class="ingredient" style="left:120px; top:396px;">
      <svg class="ingredient-icon" width="70" height="70" viewBox="0 0 70 70"><circle cx="35" cy="35" r="32" fill="none" stroke="var(--ink-white)" stroke-width="2"/><circle role="img" aria-label="Line drawing of a cow" cx="35" cy="35" r="24" fill="var(--icon-tone)"/></svg>
      <p class="ingredient-name">STEAK</p>
      <span class="ingredient-line"></span>
    </div>
    <div class="ingredient" style="left:120px; top:502px;">
      <svg class="ingredient-icon" width="70" height="70" viewBox="0 0 70 70"><circle cx="35" cy="35" r="32" fill="none" stroke="var(--ink-white)" stroke-width="2"/><circle role="img" aria-label="Line drawing of a tomato" cx="35" cy="35" r="24" fill="var(--icon-tone)"/></svg>
      <p class="ingredient-name">TOMATOES</p>
      <span class="ingredient-line"></span>
    </div>
    <div class="ingredient" style="left:120px; top:608px;">
      <svg class="ingredient-icon" width="70" height="70" viewBox="0 0 70 70"><circle cx="35" cy="35" r="32" fill="none" stroke="var(--ink-white)" stroke-width="2"/><circle role="img" aria-label="Line drawing of an onion" cx="35" cy="35" r="24" fill="var(--icon-tone)"/></svg>
      <p class="ingredient-name">ONIONS</p>
      <span class="ingredient-line"></span>
    </div>
    <div class="ingredient" style="left:120px; top:713px;">
      <svg class="ingredient-icon" width="70" height="70" viewBox="0 0 70 70"><circle cx="35" cy="35" r="32" fill="none" stroke="var(--ink-white)" stroke-width="2"/><circle role="img" aria-label="Line drawing of rice grains" cx="35" cy="35" r="24" fill="var(--icon-tone)"/></svg>
      <p class="ingredient-name">RICE</p>
      <span class="ingredient-line"></span>
    </div>
  </section>

  <section class="col-right">
    <div class="ingredient" style="left:634px; top:291px;">
      <svg class="ingredient-icon" width="70" height="70" viewBox="0 0 70 70"><circle cx="35" cy="35" r="32" fill="none" stroke="var(--ink-white)" stroke-width="2"/><circle role="img" aria-label="Line drawing of a garlic bulb" cx="35" cy="35" r="24" fill="var(--icon-tone)"/></svg>
      <p class="ingredient-name">GARLIC</p>
      <span class="ingredient-line"></span>
    </div>
    <div class="ingredient" style="left:634px; top:396px;">
      <svg class="ingredient-icon" width="70" height="70" viewBox="0 0 70 70"><circle cx="35" cy="35" r="32" fill="none" stroke="var(--ink-white)" stroke-width="2"/><circle role="img" aria-label="Line drawing of a bell pepper" cx="35" cy="35" r="24" fill="var(--icon-tone)"/></svg>
      <p class="ingredient-name">BELL PEPPERS</p>
      <span class="ingredient-line"></span>
    </div>
    <div class="ingredient" style="left:634px; top:502px;">
      <svg class="ingredient-icon" width="70" height="70" viewBox="0 0 70 70"><circle cx="35" cy="35" r="32" fill="none" stroke="var(--ink-white)" stroke-width="2"/><circle role="img" aria-label="Line drawing of ginger root" cx="35" cy="35" r="24" fill="var(--icon-tone)"/></svg>
      <p class="ingredient-name">GINGER ROOT</p>
      <span class="ingredient-line"></span>
    </div>
    <div class="ingredient" style="left:634px; top:608px;">
      <svg class="ingredient-icon" width="70" height="70" viewBox="0 0 70 70"><circle cx="35" cy="35" r="32" fill="none" stroke="var(--ink-white)" stroke-width="2"/><circle role="img" aria-label="Line drawing of a habanero pepper" cx="35" cy="35" r="24" fill="var(--icon-tone)"/></svg>
      <p class="ingredient-name">HABANERO<br>PEPPERS</p>
      <span class="ingredient-line"></span>
    </div>
    <div class="ingredient" style="left:634px; top:713px;">
      <svg class="ingredient-icon" width="70" height="70" viewBox="0 0 70 70"><circle cx="35" cy="35" r="32" fill="none" stroke="var(--ink-white)" stroke-width="2"/><circle role="img" aria-label="Line drawing of a hand sprinkling spices" cx="35" cy="35" r="24" fill="var(--icon-tone)"/></svg>
      <p class="ingredient-name">SPICE BLEND</p>
      <span class="ingredient-line"></span>
    </div>
  </section>
</main>
</body>
</html>
```